Boutique Fitness Facility needs a new meal plan design that is as hot as our workouts!

We are about to host our 6 week Coral Tide program and we need to have a great looking meal plan handout created that we can give to all of our participants.

I have attached an example of our current full meal plan, for a reference only.

As in the example I've provided, I'd like to have certain areas color coded such as the proteins being Blue, Fats -yellow, Carbs - orange and veggies- green.

These colors will corollate to the Breakfast - snack - lunch - snack - Dinner graph that I've provided and would like to have added to the new handout.

I would like our logo placed at the top and beneath the logo have the text "Coral Tide Challenge"

The flyer should be of a summer influence in colors and design and
All text should be easy to read.

Thank you and I look forward to seeing your design!

```html
<!DOCTYPE html>
<html lang="en">
<head>
<meta charset="utf-8">
<title>Vantra Fit – Coral Tide Challenge Meal Plan</title>
<link href="https://fonts.googleapis.com/css2?family=Montserrat:wght@800&family=Roboto+Condensed:wght@400;700&display=swap" rel="stylesheet">
<style>
:root{
  --protein:#1a6fc0;
  --protein-dark:#134f8c;
  --fats:#fcd716;
  --fats-dark:#e5a813;
  --carbs:#f58a1f;
  --carbs-dark:#e8541e;
  --veg:#22a35a;
  --veg-dark:#137a3b;
  --ink:#1d1d1d;
  --card:#f4f4f6;
  --navy:#262a4f;
  --gold:#f7d51d;
}
*{margin:0;padding:0;box-sizing:border-box}
html,body{width:1200px;height:1200px;overflow:hidden;background:#fff}
body{position:relative;font-family:"Roboto Condensed",Arial,sans-serif;color:var(--ink)}
.flyer{position:absolute;left:225px;top:114px;width:758px;height:980px;overflow:hidden;
  background:linear-gradient(180deg,#3a2a7a 0%,#5a2f86 14%,#3b3f9a 30%,#4c3b6e 42%,#6b6444 52%,#8a8058 62%,#9b9070 70%,#6fb9c9 76%,#bde3e6 86%,#f3e1b8 100%)}
.hero-photo{position:absolute;left:0;top:0;width:758px;height:330px;
  background:linear-gradient(160deg,#b2305a 0%,#6b2b8f 35%,#2e49b0 65%,#5b2f88 100%);opacity:.85}
.grunge{position:absolute;left:0;top:470px;width:758px;height:220px;
  background:radial-gradient(ellipse at 50% 40%,#c9bd8c 0%,#857a52 60%,#5e5840 100%);opacity:.9}
.beach{position:absolute;left:0;top:700px;width:758px;height:280px;
  background:linear-gradient(180deg,#7fc4d3 0%,#c7e6e4 45%,#f2dfb4 100%)}
.palm-left,.palm-right{position:absolute;top:290px;width:60px;height:330px;background:linear-gradient(180deg,#2f7a4a,#1d5a36)}
.palm-left{left:0;border-radius:0 60px 60px 0}
.palm-right{right:0;border-radius:60px 0 0 60px}
.ring-left,.ring-right{position:absolute;top:730px;width:90px;height:200px;background:linear-gradient(180deg,#e0453f,#f7f1ea 50%,#3c8d5a)}
.ring-left{left:0;border-radius:0 80px 40px 0}
.ring-right{right:0;border-radius:80px 0 0 40px}
.leaves-bottom{position:absolute;left:0;bottom:0;width:758px;height:60px;background:linear-gradient(180deg,rgba(46,122,70,0),#2e7a46)}

.brand{position:absolute;left:0;width:758px;top:36px;text-align:center;color:#fff;font-weight:700;font-size:60px;line-height:62px;letter-spacing:1px;text-transform:uppercase}
.brand-tag{position:absolute;left:0;width:758px;top:112px;text-align:center;color:var(--gold);font-weight:700;font-size:9.5px;letter-spacing:3px}

.title-band{position:absolute;left:39px;top:157px;width:680px;height:38px;border-radius:4px;
  background:linear-gradient(90deg,#1aa6e0 0%,#f6a81e 30%,#f08a1f 55%,#a7b43a 80%,#2fb04a 100%);
  display:flex;align-items:center;justify-content:center;
  font-family:Montserrat,Arial,sans-serif;font-weight:800;font-size:20px;color:#fff;letter-spacing:.3px}

.card{position:absolute;top:236px;height:251px;background:var(--card);border-radius:8px;padding:36px 0 0 10px}
.card-protein{left:39px;width:172px}
.card-fats{left:221px;width:153px}
.card-carbs{left:384px;width:154px}
.card-veg{left:548px;width:171px}
.tab{position:absolute;top:217px;height:37px;display:flex;align-items:center;justify-content:center;
  font-weight:700;font-size:13px;color:#fff;border-radius:3px 3px 12px 3px}
.tab-protein{left:53px;width:120px;background:var(--protein)}
.tab-fats{left:258px;width:101px;background:var(--fats);color:#222}
.tab-carbs{left:398px;width:102px;background:var(--carbs)}
.tab-veg{left:586px;width:119px;background:var(--veg)}

.food-list{list-style:none;font-size:11.3px;line-height:18.2px}
.food-list li{display:flex;align-items:flex-start;gap:6px}
.dot{flex:none;width:8px;height:8px;margin-top:5px;border-radius:50%}
.cup{flex:none;width:7px;height:8px;margin-top:5px;clip-path:polygon(0 0,100% 0,80% 100%,20% 100%)}
.food-list.protein .dot{background:var(--protein)}
.food-list.fats .dot{background:var(--fats-dark)}
.food-list.carbs .cup,.food-list.carbs .dot{background:var(--carbs)}
.food-list.veg .cup{background:var(--veg)}
.indent{padding-left:14px}

.note{position:absolute;left:561px;top:414px;width:146px;height:50px;border:1.5px solid var(--veg);font-size:8.6px;line-height:14px;padding:9px 0 0 4px}
.note-title{position:absolute;top:-8px;left:0;width:100%;text-align:center;font-size:10.5px}
.note-title span{background:var(--card);padding:0 6px}

.meal{position:absolute;top:514px;width:118px;height:118px}
.meal-breakfast{left:48px}.meal-lunch{left:319px}.meal-dinner{left:591px}
.meal-label{position:absolute;inset:0;display:flex;align-items:center;justify-content:center;font-weight:700;font-size:15px;color:#111;letter-spacing:.2px}
.meal-dinner .meal-label,.meal-lunch .meal-label{font-size:16px}

.snack{position:absolute;top:558px;width:135px}
.snack-1{left:176px}.snack-2{left:448px}
.snack-arrows{position:absolute;top:-32px;left:20px;width:95px;height:24px}
.snack-label{position:relative;z-index:2;margin:0 14px;height:30px;background:var(--veg);border-radius:3px 3px 10px 10px;
  display:flex;align-items:center;justify-content:center;color:#fff;font-weight:700;font-size:11.5px;font-family:Montserrat,Arial,sans-serif}
.snack-box{margin-top:-14px;height:44px;background:var(--navy);border:1px solid var(--veg);clip-path:polygon(10% 0,90% 0,100% 100%,0 100%);
  display:flex;align-items:flex-end;justify-content:center;padding-bottom:8px;color:#fff;font-size:11px}

.guide{position:absolute;left:91px;top:676px;width:577px;height:250px;background:rgba(255,255,255,.95);border-radius:6px}
.guide-band{position:absolute;left:125px;top:659px;width:508px;height:37px;border-radius:4px;
  background:linear-gradient(90deg,#1aa6e0 0%,#f6a81e 30%,#f08a1f 55%,#a7b43a 80%,#2fb04a 100%);
  display:flex;align-items:center;justify-content:center;font-family:Montserrat,Arial,sans-serif;font-weight:800;font-size:19px;color:#fff}
.guide-body{position:absolute;left:125px;top:710px;width:508px;font-size:10.6px;line-height:14.8px;text-align:justify}
.guide-body ol{margin-top:9px;padding-left:15px}
.guide-body li{margin-bottom:3.5px;padding-left:2px}

.footer-url{position:absolute;left:0;width:758px;top:940px;text-align:center;font-weight:700;font-size:14px;color:#111}
</style>
</head>
<body>
<main class="flyer">
  <div class="hero-photo" role="img" aria-label="Group fitness class working out under colourful neon studio lights"></div>
  <div class="grunge" role="img" aria-label="Textured cracked earth backdrop"></div>
  <div class="beach" role="img" aria-label="Summer beach scene with sea and sand"></div>
  <div class="palm-left" role="img" aria-label="Tropical palm leaves"></div>
  <div class="palm-right" role="img" aria-label="Tropical palm leaves"></div>
  <div class="ring-left" role="img" aria-label="Life ring and beach ball"></div>
  <div class="ring-right" role="img" aria-label="Life ring and beach ball"></div>
  <div class="leaves-bottom" role="img" aria-label="Tropical foliage border"></div>

  <div class="brand">Vantra Fit</div>
  <div class="brand-tag">PERSONAL GROUP TRAINING</div>

  <h1 class="title-band">CORAL TIDE CHALLENGE</h1>

  <section class="card card-protein">
    <ul class="food-list protein">
      <li><i class="dot"></i>4-6 oz Chicken Breast</li>
      <li><i class="dot"></i>4-6 oz Turkey Breast</li>
      <li><i class="dot"></i>4-6 oz Filet Mignon</li>
      <li><i class="dot"></i>4-6 oz Flank Steak</li>
      <li><i class="dot"></i>4-6 oz Salmon</li>
      <li><i class="dot"></i>4-6 oz Tuna</li>
      <li><i class="dot"></i>4-6 oz Cod</li>
      <li><i class="dot"></i>4-6 oz Cottage Cheese</li>
      <li><i class="dot"></i>4-6 oz Greek Yogurt</li>
      <li><i class="dot"></i>4-6 oz Tofu</li>
      <li><i class="dot"></i>3-5 egg whites + 1 whole egg</li>
    </ul>
  </section>
  <section class="card card-fats">
    <ul class="food-list fats">
      <li><i class="dot"></i>¼ - ½ Avocado</li>
      <li><i class="dot"></i>1 tbs Olive Oil</li>
      <li><i class="dot"></i>1 small handful Almonds,</li>
      <li class="indent">Walnuts, Cashews</li>
    </ul>
  </section>
  <section class="card card-carbs">
    <ul class="food-list carbs">
      <li><i class="cup"></i>3 - 4 oz Sweet Potato</li>
      <li><i class="cup"></i>¼ - ½ cup White Rice</li>
      <li><i class="cup"></i>¼ - ½ cup Quinoa</li>
      <li><i class="cup"></i>¼ - ½ cup Oatmeal</li>
      <li><i class="dot"></i>¾ cup Blueberries</li>
      <li><i class="cup"></i>¾ cup Strawberries</li>
      <li><i class="cup"></i>¾ cup Raspberries</li>
      <li><i class="dot"></i>1 med. Apple</li>
      <li><i class="dot"></i>1 small orange</li>
      <li><i class="dot"></i>1 small grapefruit</li>
    </ul>
  </section>
  <section class="card card-veg">
    <ul class="food-list veg">
      <li><i class="cup"></i>1 Scoop Powdered Greens</li>
      <li><i class="cup"></i>1 Cup Sautéed Spinach</li>
      <li><i class="cup"></i>1 Cup Sautéed Kale, Broccoli</li>
      <li><i class="cup"></i>1 Cup Sautéed Bell Pepper</li>
      <li><i class="cup"></i>1 Cup Sautéed Carrots</li>
      <li><i class="cup"></i>1 Cup Sautéed Zucchini</li>
    </ul>
  </section>
  <div class="note"><div class="note-title"><span>Note:</span></div>&lt; 150 lbs stick to smaller portions<br>&gt; 150 lbs stick to larger portions.</div>

  <div class="tab tab-protein">PROTEIN</div>
  <div class="tab tab-fats">FATS</div>
  <div class="tab tab-carbs">CARBS</div>
  <div class="tab tab-veg">VEGETABLES</div>

  <svg width="0" height="0" style="position:absolute">
    <defs>
      <radialGradient id="silver" cx="45%" cy="35%" r="70%">
        <stop offset="0" stop-color="#ffffff"/><stop offset=".6" stop-color="#d4d4d8"/><stop offset="1" stop-color="#8c8c94"/>
      </radialGradient>
      <g id="meal-ring">
        <circle cx="59" cy="59" r="57" fill="#2a2d55"/>
        <path d="M16 70 A44 44 0 0 1 59 15" fill="none" stroke="#f58a1f" stroke-width="14"/>
        <path d="M62 15 A44 44 0 0 1 94 85" fill="none" stroke="#1a8ad8" stroke-width="14"/>
        <path d="M92 88 A44 44 0 0 1 18 74" fill="none" stroke="#2bb04e" stroke-width="14"/>
        <circle cx="59" cy="59" r="38" fill="url(#silver)"/>
        <text x="16" y="42" font-size="11" font-weight="700" fill="#111" font-family="Roboto Condensed,sans-serif">1</text>
        <text x="97" y="42" font-size="11" font-weight="700" fill="#111" font-family="Roboto Condensed,sans-serif">1</text>
        <text x="56" y="114" font-size="11" font-weight="700" fill="#111" font-family="Roboto Condensed,sans-serif">1</text>
      </g>
      <g id="snack-arrow">
        <path d="M4 22 Q8 4 30 6" fill="none" stroke="#1a8ad8" stroke-width="6"/>
        <path d="M26 0 L40 7 L26 14Z" fill="#1a8ad8"/>
      </g>
    </defs>
  </svg>

  <div class="meal meal-breakfast"><svg width="118" height="118"><use href="#meal-ring"/></svg><div class="meal-label">BREAKFAST</div></div>
  <div class="meal meal-lunch"><svg width="118" height="118"><use href="#meal-ring"/></svg><div class="meal-label">LUNCH</div></div>
  <div class="meal meal-dinner"><svg width="118" height="118"><use href="#meal-ring"/></svg><div class="meal-label">DINNER</div></div>

  <div class="snack snack-1">
    <svg class="snack-arrows" viewBox="0 0 95 24"><use href="#snack-arrow"/><use href="#snack-arrow" x="48"/></svg>
    <div class="snack-label">SNACK</div>
    <div class="snack-box">½ Portion of Protein</div>
  </div>
  <div class="snack snack-2">
    <svg class="snack-arrows" viewBox="0 0 95 24"><use href="#snack-arrow"/><use href="#snack-arrow" x="48"/></svg>
    <div class="snack-label">SNACK</div>
    <div class="snack-box">½ Portion of Protein</div>
  </div>

  <section class="guide"></section>
  <h2 class="guide-band">FUEL YOUR CORAL TIDE!</h2>
  <div class="guide-body">
    <p>This plan isn't about starving yourself - it's about sculpting a lean, toned physique by shredding fat while preserving muscle. Here's how to maximize your results:</p>
    <ol>
      <li>Eat Like a Champion: Stick to this list as close as possible for maximum results, 7 Days A Week.</li>
      <li>Burn More Than You Consume: This is the golden rule! You need to burn more calories than you consume to create a deficit and force your body to tap into fat stores for energy.</li>
      <li>Prioritize Protein: Protein helps build and maintain muscle mass, which is crucial for boosting metabolism and burning more calories at rest.</li>
      <li>Maximize Sleep: When sleep-deprived, your body produces more ghrelin (hunger hormone) and less leptin (satiety hormone). Aim for 7-8 hours of quality sleep nightly.</li>
      <li>Consistency is King/Queen Don't expect overnight results. Stick to your plan, track your progress, and celebrate small victories. Remember, slow and steady wins the shred race!</li>
    </ol>
  </div>

  <div class="footer-url">www.joinvantrafit.com</div>
</main>
</body>
</html>
```